Florida-based Coastal Landscaping Comapny Needs Postcard Designs

We are a newly established Florida-based, coastal landscaping company that is looking for some really innovative postcards that we can use to get our name our to affluent consumers that live on the coast of Florida (think on the beach) and small to medium sized businesses in the same area. We will be sending out 100s of thousands of these, so need a great design

Target Market(s)

Affluent consumers and small to medium sized businesses

Industry/Entity Type

Landscaping

Font styles to use
Sans Serif

Colors

Designer to choose colors to be used in the design.

Requirements
Must have
• Florida - looking, island looking / paradise, but incorporate landscaping themes
• Need to say something about "Enjoy your yard this summer" or something relating to summer, landscapes and florida
• and would like to make two offers $50.00 off with signing up for one of our routine maintenance programs, or 1 free landscape inspection
Should not have
• Regular generic lawn company designs. We are a top tier landscape design / build plus maintenance firm, so not your mom and pop lawn mowing company

```html
<!DOCTYPE html>
<html lang="en">
<head>
<meta charset="utf-8">
<title>Tidegrove Landscaping Postcard</title>
<link rel="stylesheet" href="https://fonts.googleapis.com/css2?family=Questrial&family=Roboto+Condensed:wght@700&family=Arimo:wght@700&family=Kaushan+Script&family=Open+Sans:ital@1&display=swap">
<style>
  :root {
    --sky: #5fb4e8;
    --lawn: #4d8f2e;
    --house: #b9c7a4;
    --brand-blue: #00aeef;
    --logo-blue: #1a8fc4;
    --ink: #333a40;
    --charcoal: #363a40;
    --white: #ffffff;
    --ribbon: #d8191f;
    --page: #ffffff;
  }
  * { margin: 0; padding: 0; box-sizing: border-box; }
  html, body { width: 787px; height: 1200px; overflow: hidden; background: var(--page); }
  body { position: relative; font-family: "Questrial", sans-serif; }

  .card { position: absolute; left: 31px; width: 692px; overflow: hidden; background: var(--white); border: 1px solid #e2e2e2; }
  .card--front { top: 31px; height: 536px; }
  .card--back { top: 593px; height: 541px; }

  /* Front */
  .hero-photo {
    position: absolute; left: 0; top: 0; width: 100%; height: 340px;
    background: linear-gradient(180deg, var(--sky) 0%, #cfe3ee 28%, var(--house) 45%, #8c9c78 65%, #5d7f3a 80%, var(--lawn) 100%);
  }
  .hero-headline {
    position: absolute; left: 0; right: 0; top: 272px; text-align: center;
    font-family: "Kaushan Script", cursive; font-weight: 400; font-size: 40px; color: var(--white);
    text-shadow: 1px 2px 3px rgba(0,0,0,.45); letter-spacing: .5px; line-height: 1.2;
  }
  .front-contact {
    position: absolute; left: 0; top: 340px; width: 284px; height: 196px;
    background: var(--white); text-align: center;
  }
  .brand-name {
    font-family: "Questrial", sans-serif; color: var(--logo-blue);
    font-size: 30px; letter-spacing: 1.5px;
  }
  .front-contact .brand-name { margin-top: 37px; }
  .contact-line {
    display: flex; align-items: center; justify-content: center; gap: 8px;
    color: var(--brand-blue); font-family: "Questrial", sans-serif;
  }
  .front-contact .contact-line--phone { margin-top: 20px; font-size: 24px; }
  .front-contact .contact-line--web { margin-top: 8px; font-size: 19px; }
  .contact-line svg { flex: none; }

  .front-services {
    position: absolute; left: 284px; top: 340px; right: 0; height: 196px;
    background: var(--brand-blue); color: var(--white); text-align: center;
  }
  .services-title { margin-top: 22px; font-size: 26px; line-height: 37px; letter-spacing: .5px; }
  .services-list {
    margin-top: 12px; font-family: "Roboto Condensed", sans-serif; font-weight: 700;
    font-size: 17px; letter-spacing: 1px;
  }
  .services-list .star { margin: 0 6px; font-size: 15px; }
  .services-note { margin-top: 18px; font-family: "Open Sans", sans-serif; font-style: italic; font-size: 16px; }

  /* Back */
  .back-panel { position: absolute; left: 0; top: 0; width: 330px; height: 100%; }
  .back-brand { height: 86px; display: flex; align-items: center; justify-content: center; }
  .back-contact {
    height: 71px; background: var(--charcoal); color: var(--white);
    display: flex; flex-direction: column; justify-content: center; gap: 6px;
  }
  .back-contact .contact-line { color: var(--white); font-family: "Arimo", sans-serif; font-weight: 700; font-size: 19px; }
  .back-offers { position: absolute; top: 157px; left: 0; width: 330px; bottom: 0; background: var(--brand-blue); }

  .coupon {
    position: absolute; left: 26px; width: 278px; height: 109px;
    border: 2px dashed var(--white); color: var(--white); text-align: center;
  }
  .coupon--discount { top: 26px; }
  .coupon--inspection { top: 153px; }
  .coupon-ribbon { position: absolute; left: -2px; top: -2px; }
  .coupon-body { position: absolute; left: 55px; right: 8px; top: 0; bottom: 0; display: flex; flex-direction: column; justify-content: center; font-family: "Arimo", sans-serif; font-weight: 700; }
  .coupon-headline { font-size: 24px; line-height: 1.1; }
  .coupon-detail { font-family: "Roboto Condensed", sans-serif; font-size: 14.5px; line-height: 1.5; }
  .coupon--inspection .coupon-body { padding-bottom: 10px; }

  .back-tagline {
    position: absolute; left: 0; right: 0; top: 288px; text-align: center;
    font-family: "Kaushan Script", cursive; font-weight: 400; color: var(--white); font-size: 17px; line-height: 31px;
  }
  .address-area { position: absolute; left: 330px; top: 0; right: 0; bottom: 0; background: var(--white); }
</style>
</head>
<body>

<section class="card card--front">
  <div class="hero-photo" role="img" aria-label="Photo of a sage green Florida home with palm trees, tropical flower beds and a lush green lawn beside a lake"></div>
  <h1 class="hero-headline">Sit back and enjoy your summer!</h1>

  <div class="front-contact">
    <div class="brand-name">TIDEGROVE</div>
    <div class="contact-line contact-line--phone">
      <svg width="15" height="20" viewBox="0 0 15 20" aria-hidden="true"><path d="M3 1 L6 1 L7 6 L5 7.5 C5.5 10.5 7 13 9 14.5 L11 13 L14 16 L12 19 C5 18 1 10 1 3 Z" fill="#555"/></svg>
      <span>555-214-7390</span>
    </div>
    <div class="contact-line contact-line--web">
      <svg width="17" height="17" viewBox="0 0 20 20" aria-hidden="true"><g fill="none" stroke="#444" stroke-width="1.5"><circle cx="10" cy="10" r="8.5"/><ellipse cx="10" cy="10" rx="3.8" ry="8.5"/><line x1="1.5" y1="10" x2="18.5" y2="10"/><line x1="3" y1="5.5" x2="17" y2="5.5"/><line x1="3" y1="14.5" x2="17" y2="14.5"/></g></svg>
      <span>www.tidegroveco.com</span>
    </div>
  </div>

  <div class="front-services">
    <p class="services-title">Residential &amp; Commercial<br>LANDSCAPING SERVICES</p>
    <p class="services-list">DESIGN<span class="star">★</span>INSTALLATION<span class="star">★</span>MAINTENANCE</p>
    <p class="services-note">See special offers on back!</p>
  </div>
</section>

<section class="card card--back">
  <div class="back-panel">
    <div class="back-brand"><div class="brand-name">TIDEGROVE</div></div>
    <div class="back-contact">
      <div class="contact-line">
        <svg width="14" height="19" viewBox="0 0 15 20" aria-hidden="true"><path d="M3 1 L6 1 L7 6 L5 7.5 C5.5 10.5 7 13 9 14.5 L11 13 L14 16 L12 19 C5 18 1 10 1 3 Z" fill="#fff"/></svg>
        <span>555-214-7390</span>
      </div>
      <div class="contact-line">
        <svg width="19" height="19" viewBox="0 0 20 20" aria-hidden="true"><g fill="none" stroke="#fff" stroke-width="1.6"><circle cx="10" cy="10" r="8.5"/><ellipse cx="10" cy="10" rx="3.8" ry="8.5"/><line x1="1.5" y1="10" x2="18.5" y2="10"/><line x1="3" y1="5.5" x2="17" y2="5.5"/><line x1="3" y1="14.5" x2="17" y2="14.5"/></g></svg>
        <span>www.tidegroveco.com</span>
      </div>
    </div>

    <div class="back-offers">
      <div class="coupon coupon--discount">
        <svg class="coupon-ribbon" width="76" height="76" viewBox="0 0 76 76" aria-hidden="true">
          <polygon points="0,0 76,0 0,76" fill="var(--ribbon)"/>
          <text x="24" y="34" transform="rotate(-45 24 34)" text-anchor="middle" font-family="Arimo, sans-serif" font-size="10" fill="#fff">Special</text>
          <text x="30" y="42" transform="rotate(-45 30 42)" text-anchor="middle" font-family="Arimo, sans-serif" font-size="10" fill="#fff">Offer!</text>
        </svg>
        <div class="coupon-body">
          <div class="coupon-headline">$50.00 off</div>
          <div class="coupon-detail">When you sign up for one of our<br>maintenance programs.</div>
        </div>
      </div>

      <div class="coupon coupon--inspection">
        <svg class="coupon-ribbon" width="76" height="76" viewBox="0 0 76 76" aria-hidden="true">
          <polygon points="0,0 76,0 0,76" fill="var(--ribbon)"/>
          <text x="24" y="34" transform="rotate(-45 24 34)" text-anchor="middle" font-family="Arimo, sans-serif" font-size="10" fill="#fff">Special</text>
          <text x="30" y="42" transform="rotate(-45 30 42)" text-anchor="middle" font-family="Arimo, sans-serif" font-size="10" fill="#fff">Offer!</text>
        </svg>
        <div class="coupon-body">
          <div class="coupon-headline">FREE</div>
          <div class="coupon-detail">LANDSCAPE INSPECTION</div>
        </div>
      </div>

      <p class="back-tagline">We are committed to high quality work<br>and outstanding customer service!</p>
    </div>
  </div>
  <div class="address-area"></div>
</section>

</body>
</html>
```